An our door sign really promoting our clinic and services

We have a new sports medicine clinic called ASHBRAE SPORTS MEDICINE.
We want to make a really nice external sign at our clinic using a photo of our team we really like. I have attached the photo.
We want to simply include our LOGO and also signs with these slogan options. So we want different signs with these different slogans so we can choose what we really like.
This should be a simple and quite design.

The SLOGANS WE WOULD LIKE TO SEE ON THE SIGN (only one slogan per sign in the drafts)

1. Your Journey. Our Expertise
2. Where better health begins
3. Building the best version of you
4. Your health, in expert hands
5. Reaching new heights in your health
6. Your path to peak performance starts here

I have also included different versions of our logo based on the background and how you set the sign up

So summary
1. Image attached
2. Slogan options we would like to see them all
3. Logo attached (various options based on how you set the background up)
4. Size of sign is 2935mm wide x 1885mm high

```html
<!DOCTYPE html>
<html lang="en">
<head>
<meta charset="utf-8">
<title>Ashbrae Sports Medicine – Where Better Health Begins</title>
<link rel="stylesheet" href="https://fonts.googleapis.com/css2?family=Poppins:ital,wght@0,800;1,800&display=swap">
<style>
  :root {
    --backdrop: #d5d6d8;
    --edge: #ffffff;
    --navy-deep: #001c52;
    --navy: #0a3170;
    --navy-mid: #0d3f80;
    --sky: #52c4ea;
    --mist: #dfe3e8;
    --white: #ffffff;
  }
  html, body {
    margin: 0;
    width: 1200px;
    height: 802px;
    overflow: hidden;
    background: var(--backdrop);
  }
  .stage { position: relative; width: 1200px; height: 802px; }
  .sign-edge {
    position: absolute; left: 113px; top: 51px;
    width: 1013px; height: 651px; background: var(--edge);
  }
  .sign {
    position: absolute; left: 117px; top: 48px;
    width: 1011px; height: 649px; display: block;
  }
  .brand-name {
    font-family: "Poppins", sans-serif;
    font-weight: 800;
    fill: var(--white);
    letter-spacing: 1px;
  }
  .slogan { font-family: "Poppins", sans-serif; font-weight: 800; font-style: italic; }
  .slogan-white { fill: var(--white); }
  .slogan-sky { fill: var(--sky); }
</style>
</head>
<body>
<div class="stage">
  <div class="sign-edge"></div>
  <svg class="sign" viewBox="0 0 1011 649" xmlns="http://www.w3.org/2000/svg">
    <defs>
      <linearGradient id="panelFill" x1="0" y1="0" x2="1" y2="1">
        <stop offset="0" stop-color="var(--navy)"/>
        <stop offset="0.55" stop-color="var(--navy-deep)"/>
        <stop offset="1" stop-color="var(--navy-deep)"/>
      </linearGradient>
      <linearGradient id="photoFill" x1="0" y1="0" x2="1" y2="1">
        <stop offset="0" stop-color="#e6e8ea"/>
        <stop offset="0.5" stop-color="#8b8e93"/>
        <stop offset="1" stop-color="#2a2f36"/>
      </linearGradient>
      <linearGradient id="glassFill" x1="0" y1="0" x2="1" y2="0">
        <stop offset="0" stop-color="#1a5aa0" stop-opacity="0.7"/>
        <stop offset="1" stop-color="#1a5aa0" stop-opacity="0.15"/>
      </linearGradient>
    </defs>

    <rect class="panel" width="1011" height="649" fill="url(#panelFill)"/>

    <g class="accent-bands">
      <polygon points="1000,0 1011,0 1011,131 898,131 990,0" fill="var(--navy-mid)" opacity="0.6"/>
      <polygon points="921,19 1011,19 1011,62 895,62" fill="url(#glassFill)"/>
      <polygon points="600,337 1011,337 1011,500 520,500" fill="var(--navy-mid)" opacity="0.35"/>
      <polygon points="750,440 1011,440 1011,550 700,550" fill="var(--navy-mid)" opacity="0.25"/>
      <polygon points="840,437 990,437 960,480 815,480" fill="#0d4fa0" opacity="0.6"/>
      <g stroke="#0c2550" stroke-width="1" fill="none">
        <line x1="838" y1="61" x2="875" y2="19"/>
        <line x1="864" y1="61" x2="901" y2="19"/>
        <line x1="890" y1="61" x2="927" y2="19"/>
      </g>
      <g stroke="#3a7cc4" stroke-width="1" opacity="0.6">
        <line x1="960" y1="456" x2="980" y2="421"/>
        <line x1="972" y1="456" x2="992" y2="421"/>
        <line x1="984" y1="456" x2="1004" y2="421"/>
      </g>
      <g stroke="#1d4c8a" stroke-width="1" opacity="0.7">
        <line x1="491" y1="578" x2="538" y2="515"/>
        <line x1="500" y1="578" x2="547" y2="515"/>
        <line x1="509" y1="578" x2="556" y2="515"/>
        <line x1="518" y1="578" x2="565" y2="515"/>
      </g>
    </g>

    <g class="brand">
      <text class="brand-name" x="60" y="82" font-size="38" textLength="560" lengthAdjust="spacingAndGlyphs">ASHBRAE SPORTS MEDICINE</text>
    </g>

    <polygon class="photo-frame" points="3,141 630,141 377,581 3,581"
             fill="url(#photoFill)" role="img"
             aria-label="Photo of a clinician in a navy polo reviewing a tablet with a client in the clinic gym"/>
    <polygon points="3,141 32,141 3,301" fill="var(--sky)"/>
    <polygon points="48,115 128,115 116,136 36,136" fill="var(--navy)"/>
    <polygon points="32,136 116,136 101,171 16,171" fill="#0a3576"/>
    <polygon points="526,347 559,347 476,492 451,492" fill="var(--mist)"/>
    <polygon points="531,297 564,297 415,555 381,555" fill="var(--sky)"/>

    <g class="slogan" text-anchor="end" font-size="85">
      <text class="slogan-white" x="950" y="208">WHERE</text>
      <text class="slogan-sky" x="952" y="318">BETTER</text>
      <text class="slogan-white" x="952" y="428">HEALTH</text>
      <text class="slogan-sky" x="952" y="537">BEGINS</text>
    </g>
  </svg>
</div>
</body>
</html>
```